"MEET THE TEAM" page web design

We need a "meet the team" page for our website!
Please look at our website to see the style we need

We are looking for something unique, fun, cool, technology-style and yet professional. We plan on taking a picture of each employee (not sure if this will be a real photo/caricature/ black and white/goofy picture--> but we are open to any ideas you have that will work with the design) and putting it there, along with a little bio about each person.

Thanks! looking forward to working together:)
Updates

Project Deadline Extended
Reason: I am excited to see more designs and find the perfect fit. Thanks designers :)

Target Market(s)

People looking to purchase servers, workstations, components

Industry/Entity Type

Information Technology

Number of Pages Required

1 page

Font styles to use
Sans Serif
Other font styles liked:
• The font we use on our site so it matches

Requirements
Must have
• please look at our website qondimex.com and see the theme and colors we want.
• We have 13 employees but would like to have a design where we can add/remove people if we hire/terminate them without messing up the design.
• We are looking for something unique, fun, cool, technology-style and yet professional. We plan on taking a picture of each employee (not sure if this will be a real photo/caricature/ black and white/goofy picture--> but we are open to any ideas you have that will work with the design) and putting it there, along with a little bio about each person.
• We can upload anything you need
Nice to have
• We are also interested in having a design where when the cursor moves over a person then the bio comes out or moves around, or something. (This is not required, but we would love some cool ideas) And if you can come up with some design, we would have our programmers create it for us.
Should not have
• we are open to anything

```html
<!DOCTYPE html>
<html lang="en">
<head>
<meta charset="utf-8">
<title>Meet the Team – Qondimex</title>
<link href="https://fonts.googleapis.com/css2?family=Arimo:wght@400;700&display=swap" rel="stylesheet">
<style>
:root{
  --teal:#35c2b7;
  --teal-dark:#229a92;
  --ink:#333;
  --muted:#666;
  --card:#555;
  --card-edge:#444;
  --footer:#a3a3a3;
  --footer-dark:#999;
  --line:#ddd;
  --white:#fff;
}
*{box-sizing:border-box;margin:0;padding:0}
html,body{width:1002px;height:1200px;overflow:hidden;background:#fff;font-family:"Arimo",Arial,sans-serif;color:var(--ink)}
.page{position:relative;width:1002px;height:1200px}
.icon-defs{position:absolute;width:0;height:0}

/* header */
.header{position:absolute;top:0;left:0;width:100%;height:59px;border-bottom:1px solid var(--line)}
.brand{position:absolute;left:52px;top:14px;display:flex;align-items:center;gap:8px}
.brand-mark{width:24px;height:24px;background:var(--teal);border-radius:50%}
.brand-name{font-size:20px;color:var(--teal);letter-spacing:2px}
.account-tab{position:absolute;left:838px;top:0;width:113px;height:19px;background:#9d9d9d;border-radius:0 0 14px 14px;display:flex;overflow:hidden;font-size:6px;color:#eee}
.account-tab span{flex:1;display:flex;align-items:center;justify-content:center}
.account-tab span+span{background:#858585}
.contact-quick{position:absolute;top:27px;display:flex;align-items:center;gap:7px}
.circle-icon{width:26px;height:26px;border:1px solid var(--line);border-radius:50%;display:flex;align-items:center;justify-content:center}
.live-chat{left:772px;font-size:8px;color:var(--muted)}
.phone-top{left:853px;font-size:11px;color:var(--ink)}

.nav{position:absolute;top:60px;left:0;width:100%;height:29px;border-bottom:1px solid var(--line)}
.nav ul{position:absolute;left:58px;top:9px;display:flex;gap:12.4px;list-style:none;font-size:8.4px;color:#444}
.search{position:absolute;left:771px;top:66px;width:136px;height:19px;border:1px solid #ccc;border-radius:10px;font-size:6.5px;color:#555;padding:6px 0 0 17px}
.search svg{position:absolute;right:7px;top:4px}
.cart{position:absolute;left:917px;top:65px;width:23px;height:23px;border:1px solid #ccc;border-radius:50%;display:flex;align-items:center;justify-content:center}

.breadcrumb{position:absolute;top:90px;left:0;width:100%;height:21px;background:linear-gradient(90deg,var(--teal-dark),#3fd3c6 50%,var(--teal-dark));font-size:7.5px;font-weight:700;padding:7px 0 0 52px;color:#123}
.breadcrumb .home{color:var(--white)}

/* title */
.section-title{position:absolute;top:127px;left:0;width:100%;text-align:center;font-size:12.5px;font-weight:400;color:#444}
.section-title::after{content:"";display:block;width:46px;height:4px;margin:4px auto 0;border-top:1px solid #666;border-bottom:1px solid #666}

/* team grid */
.team{position:absolute;top:172px;left:52px;width:900px;display:flex;flex-wrap:wrap;justify-content:center;gap:20px 20px}
.member{width:164px;height:228px;background:var(--card);border:1px solid var(--card-edge);color:var(--white);text-align:center}
.member-photo{height:168px;background:radial-gradient(circle at 50% 40%,#b8a08a 0 22%,#8e8e8e 45%,#c9c9c9 100%)}
.member-name{font-size:8.4px;margin-top:7px}
.member-role{font-size:6.5px;margin-top:4px}
.member-links{display:flex;justify-content:center;gap:8px;margin-top:9px}
.member-links span{width:15px;height:15px;border:1px solid var(--white);display:flex;align-items:center;justify-content:center}
.member-links svg{width:9px;height:9px}
.member.is-open{background:var(--teal);border-color:var(--teal)}
.member.is-open .member-name{margin-top:25px}
.member-bio{font-size:6.7px;line-height:13.6px;padding:0 13px;margin-top:11px}
.member.is-open .member-links{margin-top:12px}

/* footer */
.footer{position:absolute;top:927px;left:0;width:100%;height:170px;background:var(--footer);color:var(--white);text-align:center}
.footer-about{width:446px;margin:13px auto 0;font-size:8.8px;line-height:11.4px}
.footer-rule{width:460px;height:1px;background:#b5b5b5;margin:7px auto 0}
.footer-contact{position:absolute;top:79px;left:0;width:100%;font-size:8.6px}
.footer-contact div{position:absolute;text-align:left;line-height:11.5px;display:flex;gap:8px}
.footer-menu{position:absolute;top:117px;left:0;width:100%;font-size:9.6px}
.footer-menu>div{position:absolute}
.footer-menu small{display:block;font-size:5.8px;line-height:8.2px;margin-top:2px}
.footer-base{position:absolute;top:1096px;left:0;width:100%;height:104px;background:var(--footer-dark);color:var(--white)}
.socials{position:absolute;top:11px;left:437px;display:flex;gap:8px}
.socials span{width:24px;height:24px;border:1px solid #ddd;border-radius:50%;display:flex;align-items:center;justify-content:center}
.socials svg{width:10px;height:10px}
.base-rule{position:absolute;top:47px;left:105px;width:780px;height:1px;background:#b3b3b3}
.copyright{position:absolute;top:57px;left:458px;display:flex;gap:6px;font-size:7.5px;line-height:10.5px}
.copyright i{width:12px;height:12px;background:#ddd;border-radius:50%;margin-top:3px}
.chat-now{position:absolute;right:0;bottom:0;width:125px;height:15px;background:var(--teal);color:var(--white);font-size:8px;font-weight:700;padding:3px 0 0 5px}
</style>
</head>
<body>
<svg class="icon-defs" aria-hidden="true">
  <defs>
    <symbol id="i-phone" viewBox="0 0 10 10"><path d="M2 1l2 2-1 1c1 1 2 2 3 3l1-1 2 2-1 1C5 9 1 5 1 2z" fill="#fff"/></symbol>
    <symbol id="i-mail" viewBox="0 0 10 10"><rect x="0.5" y="2" width="9" height="6.5" fill="#fff"/><path d="M0.5 2l4.5 3.6L9.5 2" fill="none" stroke="#555" stroke-width="0.9"/></symbol>
    <symbol id="i-link" viewBox="0 0 10 10"><rect x="0.8" y="3.3" width="5" height="3.4" rx="1.7" fill="none" stroke="#fff" stroke-width="1.1"/><rect x="4.2" y="3.3" width="5" height="3.4" rx="1.7" fill="none" stroke="#fff" stroke-width="1.1"/></symbol>
    <symbol id="i-globe" viewBox="0 0 10 10"><circle cx="5" cy="5" r="4.2" fill="none" stroke="#fff" stroke-width="1"/><ellipse cx="5" cy="5" rx="1.8" ry="4.2" fill="none" stroke="#fff" stroke-width="0.8"/><path d="M0.8 5h8.4" stroke="#fff" stroke-width="0.8"/></symbol>
    <symbol id="i-share" viewBox="0 0 10 10"><circle cx="2" cy="5" r="1.4" fill="#fff"/><circle cx="8" cy="2" r="1.4" fill="#fff"/><circle cx="8" cy="8" r="1.4" fill="#fff"/><path d="M2 5L8 2M2 5l6 3" stroke="#fff" stroke-width="0.9"/></symbol>
    <symbol id="i-chat" viewBox="0 0 10 10"><path d="M1 1.5h8v5.5H4.5L2.5 9V7H1z" fill="none" stroke="#fff" stroke-width="1"/></symbol>
  </defs>
</svg>
<div class="page">
  <header class="header">
    <div class="brand"><span class="brand-mark"></span><span class="brand-name">QONDIMEX</span></div>
    <div class="account-tab"><span>SIGN UP</span><span>LOGIN</span></div>
    <div class="contact-quick live-chat">
      <span class="circle-icon"><svg width="12" height="10" viewBox="0 0 12 10"><path d="M1 1h8v5H4l-2 2V6H1z" fill="#2fb2a8"/></svg></span>LIVE CHAT
    </div>
    <div class="contact-quick phone-top">
      <span class="circle-icon"><svg width="10" height="10" viewBox="0 0 10 10"><path d="M2 1l2 2-1 1c1 1 2 2 3 3l1-1 2 2-1 1C5 9 1 5 1 2z" fill="#2fb2a8"/></svg></span>555-204-7781
    </div>
  </header>

  <nav class="nav">
    <ul><li>SERVERS</li><li>WORKSTATIONS</li><li>COMPONENTS</li><li>VIRTUAL REALITY</li><li>DRONES</li><li>ABOUT US</li><li>BLOG</li><li>RESOURCES</li><li>CONTACT US</li></ul>
  </nav>
  <div class="search">Search<svg width="9" height="9" viewBox="0 0 9 9"><circle cx="3.6" cy="3.6" r="2.6" fill="none" stroke="#2fb2a8" stroke-width="1.3"/><path d="M5.5 5.5L8 8" stroke="#2fb2a8" stroke-width="1.4"/></svg></div>
  <div class="cart"><svg width="11" height="9" viewBox="0 0 11 9"><path d="M1 3h9l-1 5H2z" fill="none" stroke="#2fb2a8" stroke-width="1.2"/><path d="M3 3l2-2M8 3L6 1" stroke="#2fb2a8"/></svg></div>

  <div class="breadcrumb"><span class="home">HOME</span> / MEET THE TEAM</div>

  <h1 class="section-title">MEET THE TEAM</h1>

  <main class="team">
    <div class="member"><div class="member-photo" role="img" aria-label="Employee portrait photo"></div><div class="member-name">NAME OF EMPLOYEE</div><div class="member-role">Business Analyst</div><div class="member-links"><span><svg><use href="#i-phone"/></svg></span><span><svg><use href="#i-mail"/></svg></span><span><svg><use href="#i-link"/></svg></span><span><svg><use href="#i-globe"/></svg></span></div></div>
    <div class="member"><div class="member-photo" role="img" aria-label="Employee portrait photo"></div><div class="member-name">NAME OF EMPLOYEE</div><div class="member-role">Business Analyst</div><div class="member-links"><span><svg><use href="#i-phone"/></svg></span><span><svg><use href="#i-mail"/></svg></span><span><svg><use href="#i-link"/></svg></span><span><svg><use href="#i-globe"/></svg></span></div></div>
    <div class="member is-open"><div class="member-name">NAME OF EMPLOYEE</div><div class="member-role">Business Analyst</div><p class="member-bio">Aliquam et suscipit odio. Cras maximus, quam et convallis mattis, urna sem luctus leo, quis vulputate lorem nisl congue libero. Nullam eget lectus sapien. Morbi maximus interdum tempor. Pellentesque ut convallis neque.Aenean sit amet nisi feugiat libero egestas ornare. Maecenas quis bibendum ex. Proin a massa sollicitu-din</p><div class="member-links"><span><svg><use href="#i-phone"/></svg></span><span><svg><use href="#i-mail"/></svg></span><span><svg><use href="#i-link"/></svg></span><span><svg><use href="#i-globe"/></svg></span></div></div>
    <div class="member"><div class="member-photo" role="img" aria-label="Employee portrait photo"></div><div class="member-name">NAME OF EMPLOYEE</div><div class="member-role">Business Analyst</div><div class="member-links"><span><svg><use href="#i-phone"/></svg></span><span><svg><use href="#i-mail"/></svg></span><span><svg><use href="#i-link"/></svg></span><span><svg><use href="#i-globe"/></svg></span></div></div>
    <div class="member"><div class="member-photo" role="img" aria-label="Employee portrait photo"></div><div class="member-name">NAME OF EMPLOYEE</div><div class="member-role">Business Analyst</div><div class="member-links"><span><svg><use href="#i-phone"/></svg></span><span><svg><use href="#i-mail"/></svg></span><span><svg><use href="#i-link"/></svg></span><span><svg><use href="#i-globe"/></svg></span></div></div>
    <div class="member"><div class="member-photo" role="img" aria-label="Employee portrait photo"></div><div class="member-name">NAME OF EMPLOYEE</div><div class="member-role">Business Analyst</div><div class="member-links"><span><svg><use href="#i-phone"/></svg></span><span><svg><use href="#i-mail"/></svg></span><span><svg><use href="#i-link"/></svg></span><span><svg><use href="#i-globe"/></svg></span></div></div>
    <div class="member"><div class="member-photo" role="img" aria-label="Employee portrait photo"></div><div class="member-name">NAME OF EMPLOYEE</div><div class="member-role">Business Analyst</div><div class="member-links"><span><svg><use href="#i-phone"/></svg></span><span><svg><use href="#i-mail"/></svg></span><span><svg><use href="#i-link"/></svg></span><span><svg><use href="#i-globe"/></svg></span></div></div>
    <div class="member"><div class="member-photo" role="img" aria-label="Employee portrait photo"></div><div class="member-name">NAME OF EMPLOYEE</div><div class="member-role">Business Analyst</div><div class="member-links"><span><svg><use href="#i-phone"/></svg></span><span><svg><use href="#i-mail"/></svg></span><span><svg><use href="#i-link"/></svg></span><span><svg><use href="#i-globe"/></svg></span></div></div>
    <div class="member"><div class="member-photo" role="img" aria-label="Employee portrait photo"></div><div class="member-name">NAME OF EMPLOYEE</div><div class="member-role">Business Analyst</div><div class="member-links"><span><svg><use href="#i-phone"/></svg></span><span><svg><use href="#i-mail"/></svg></span><span><svg><use href="#i-link"/></svg></span><span><svg><use href="#i-globe"/></svg></span></div></div>
    <div class="member"><div class="member-photo" role="img" aria-label="Employee portrait photo"></div><div class="member-name">NAME OF EMPLOYEE</div><div class="member-role">Business Analyst</div><div class="member-links"><span><svg><use href="#i-phone"/></svg></span><span><svg><use href="#i-mail"/></svg></span><span><svg><use href="#i-link"/></svg></span><span><svg><use href="#i-globe"/></svg></span></div></div>
    <div class="member"><div class="member-photo" role="img" aria-label="Employee portrait photo"></div><div class="member-name">NAME OF EMPLOYEE</div><div class="member-role">Business Analyst</div><div class="member-links"><span><svg><use href="#i-phone"/></svg></span><span><svg><use href="#i-mail"/></svg></span><span><svg><use href="#i-link"/></svg></span><span><svg><use href="#i-globe"/></svg></span></div></div>
    <div class="member"><div class="member-photo" role="img" aria-label="Employee portrait photo"></div><div class="member-name">NAME OF EMPLOYEE</div><div class="member-role">Business Analyst</div><div class="member-links"><span><svg><use href="#i-phone"/></svg></span><span><svg><use href="#i-mail"/></svg></span><span><svg><use href="#i-link"/></svg></span><span><svg><use href="#i-globe"/></svg></span></div></div>
    <div class="member"><div class="member-photo" role="img" aria-label="Employee portrait photo"></div><div class="member-name">NAME OF EMPLOYEE</div><div class="member-role">Business Analyst</div><div class="member-links"><span><svg><use href="#i-phone"/></svg></span><span><svg><use href="#i-mail"/></svg></span><span><svg><use href="#i-link"/></svg></span><span><svg><use href="#i-globe"/></svg></span></div></div>
  </main>

  <footer class="footer">
    <p class="footer-about">Based in Delmont Park California, Qondimex offers custom servers, storage, and workstations for local businesses in Los Angeles, Beverly Hills, Thousand Oaks, Ventura, Orange County, Santa Barbara, Oxnard, Irvine, Anaheim, and San Diego. Qondimex also offers such products to clients throughout the United States and Worldwide.</p>
    <div class="footer-rule"></div>
    <div class="footer-contact">
      <div style="left:314px"><svg width="7" height="10" viewBox="0 0 7 10"><path d="M3.5 0A3.5 3.5 0 0 0 0 3.5C0 6 3.5 10 3.5 10S7 6 7 3.5A3.5 3.5 0 0 0 3.5 0z" fill="#fff"/><circle cx="3.5" cy="3.5" r="1.3" fill="#a3a3a3"/></svg><span>4820 Halvern Ave.<br>Delmont Park, CA 91400</span></div>
      <div style="left:470px"><svg width="9" height="9" viewBox="0 0 10 10"><path d="M2 1l2 2-1 1c1 1 2 2 3 3l1-1 2 2-1 1C5 9 1 5 1 2z" fill="#fff"/></svg><span>555-204-7781</span></div>
      <div style="left:606px"><svg width="9" height="7" viewBox="0 0 9 7"><rect width="9" height="7" fill="#fff"/><path d="M0 0l4.5 4L9 0" fill="none" stroke="#a3a3a3"/></svg><span>sales@qondimex.com</span></div>
    </div>
    <div class="footer-menu">
      <div style="left:261px">Computer Hardware</div>
      <div style="left:396px">Drones</div>
      <div style="left:462px">Virtual Reality</div>
      <div style="left:563px">About Us</div>
      <div style="left:656px;text-align:center">Customer Support<small>Terms and Conditions<br>Warranty Information<br>Contact Us<br>Return Policy</small></div>
    </div>
  </footer>

  <div class="footer-base">
    <div class="socials"><span><svg><use href="#i-share"/></svg></span><span><svg><use href="#i-globe"/></svg></span><span><svg><use href="#i-link"/></svg></span><span><svg><use href="#i-chat"/></svg></span></div>
    <div class="base-rule"></div>
    <div class="copyright"><i></i><span>Qondimex, LLC.<br>Copyright © 2017</span></div>
  </div>

  <div class="chat-now">CHAT NOW</div>
</div>
</body>
</html>
```